New For Sale Signs

We are looking for a design not too dissimilar to the attached. Looking more for tweaks than a radically new concept. The attached just isn't quite right. Looking to add a touch more grey (our secondary colour). We look forward to seeing your new designs!

Thank you so much for all of your creative input. We have now found the perfect design but very much appreciate your participation and wish you all the best. Kind regards, Marianne Holtsby Pellworth Estate Agents

```html
<!DOCTYPE html>
<html lang="en">
<head>
<meta charset="utf-8">
<title>Pellworth Estate Agents – For Sale Sign</title>
<link rel="stylesheet" href="https://fonts.googleapis.com/css2?family=Roboto:wght@300;400&display=swap">
<style>
  :root {
    --brand-blue: #025b7a;
    --brand-grey: #a4aeb8;
    --soft-grey: #b9c6cf;
    --white: #ffffff;
    --backdrop: #e9ecee;
  }
  * { margin: 0; padding: 0; box-sizing: border-box; }
  html, body {
    width: 957px;
    height: 1200px;
    overflow: hidden;
    background: var(--backdrop);
    font-family: "Roboto", "Helvetica Neue", Arial, sans-serif;
  }
  .sign {
    position: absolute;
    left: 143px;
    top: 97px;
    width: 669px;
    height: 1004px;
    background: var(--brand-blue);
    overflow: hidden;
  }
  .agency-name {
    position: absolute;
    left: 0;
    right: 0;
    text-align: center;
    color: var(--white);
    font-weight: 400;
    text-transform: uppercase;
    white-space: nowrap;
  }
  .agency-name--main {
    top: 65px;
    font-size: 82px;
    line-height: 90px;
    letter-spacing: 3px;
  }
  .agency-name--sub {
    top: 161px;
    font-size: 25px;
    line-height: 30px;
    letter-spacing: 7px;
  }
  .status-band {
    position: absolute;
    left: 0;
    top: 236px;
    width: 100%;
    height: 165px;
    background: var(--brand-grey);
  }
  .status-band__text {
    display: block;
    text-align: center;
    color: var(--brand-blue);
    font-weight: 300;
    font-size: 152px;
    line-height: 165px;
    letter-spacing: -2px;
  }
  .tagline {
    position: absolute;
    left: 0;
    right: 0;
    top: 404px;
    text-align: center;
    color: var(--brand-grey);
    font-weight: 300;
    font-size: 76px;
    line-height: 80px;
    letter-spacing: -1px;
    white-space: nowrap;
  }
  .enquiry-note {
    position: absolute;
    left: 0;
    right: 0;
    top: 482px;
    text-align: center;
    color: var(--brand-grey);
    font-weight: 300;
    font-size: 20.5px;
    line-height: 22px;
    white-space: nowrap;
  }
  .phone {
    position: absolute;
    left: 0;
    right: 0;
    top: 500px;
    text-align: center;
    color: var(--white);
    font-weight: 300;
    font-size: 112px;
    line-height: 116px;
    letter-spacing: 1px;
    white-space: nowrap;
  }
  .website {
    position: absolute;
    left: 0;
    right: 0;
    top: 646px;
    text-align: center;
    color: var(--soft-grey);
    font-weight: 300;
    font-size: 38.5px;
    line-height: 44px;
    white-space: nowrap;
  }
  .decor-area {
    position: absolute;
    left: 0;
    bottom: 0;
    width: 100%;
    height: 280px;
    background: linear-gradient(180deg, rgba(164,174,184,0) 0%, rgba(164,174,184,0.25) 45%, rgba(164,174,184,0.5) 100%);
  }
</style>
</head>
<body>
  <main class="sign">
    <div class="agency-name agency-name--main">Pellworth</div>
    <div class="agency-name agency-name--sub">Estate Agents</div>
    <div class="status-band"><span class="status-band__text">For Sale</span></div>
    <p class="tagline">Always.Further.</p>
    <p class="enquiry-note">For further information regarding this property please call</p>
    <p class="phone">4316 2540</p>
    <p class="website">pellworthestateagents.com.au</p>
    <div class="decor-area" role="img" aria-label="Decorative pattern of overlapping translucent grey hexagons"></div>
  </main>
</body>
</html>
```